ultra-minimalist business card

front (black background, matte):

tarik b. hosseny
writer | photographer
get@tarikhosseny.com

back (white background, matte):

a picture speaks a thousand words;
a word draws a thousand pictures.

www.tarikhosseny.com

all text should be small (white or silver - as long as it shows against the black - on the front; black or gray - as long as it shows against the white - on the back).

feel free to get creative in terms of arrangement, alignment, and font type, but remember, the overall style is minimalist, so nothing too fancy, please.

thanks.

```html
<!DOCTYPE html>
<html lang="en">
<head>
<meta charset="utf-8">
<title>tarik b. hosseny — business card</title>
<link rel="stylesheet" href="https://fonts.googleapis.com/css2?family=Ubuntu:wght@300;400;700&display=swap">
<style>
  :root {
    --backdrop: #d8ced2;
    --card-black: #050505;
    --card-edge: #1a1a1a;
    --paper-white: #f1f0ee;
    --ink: #1b1b1b;
    --ink-soft: #3a3a3a;
    --silver: #e6e6e6;
  }
  * { box-sizing: border-box; margin: 0; padding: 0; }
  html, body {
    width: 1200px;
    height: 900px;
    overflow: hidden;
    background: var(--backdrop);
    font-family: "Ubuntu", sans-serif;
  }
  .sheet {
    position: relative;
    width: 1200px;
    height: 900px;
  }
  .card {
    position: absolute;
    left: 300px;
    width: 600px;
    height: 343px;
    background: var(--card-black);
    box-shadow: 4px 5px 0 var(--card-edge), 0 10px 24px rgba(0,0,0,0.18);
  }
  .card--back  { top: 80px; }
  .card--front { top: 475px; }

  .panel {
    position: absolute;
    left: 96px;
    top: 56px;
    width: 230px;
    height: 230px;
    background: var(--paper-white);
    display: flex;
    align-items: center;
    justify-content: center;
  }

  .quote {
    text-align: center;
    color: var(--ink-soft);
    font-weight: 300;
    font-size: 14px;
    line-height: 1.3;
    white-space: nowrap;
  }
  .quote strong {
    color: var(--ink);
    font-weight: 700;
  }
  .quote .gap { display: block; height: 18px; }
  .quote .spaced { letter-spacing: 0.22em; margin-right: -0.22em; }

  .name {
    color: var(--ink);
    font-weight: 300;
    font-size: 22px;
    line-height: 1.3;
    text-align: center;
    white-space: nowrap;
  }

  .details {
    position: absolute;
    left: 372px;
    color: var(--silver);
    font-weight: 300;
    font-size: 13px;
    line-height: 1.45;
    letter-spacing: 0.01em;
    white-space: nowrap;
  }
  .card--back .details  { top: 148px; }
  .card--front .details { top: 138px; }
</style>
</head>
<body>
<main class="sheet">

  <section class="card card--back" aria-label="card back">
    <div class="panel">
      <p class="quote">
        a picture speaks a<br>
        <strong>thousand words;</strong>
        <span class="gap"></span>
        <strong class="spaced">a word draws</strong><br>
        a thousand pictures.
      </p>
    </div>
    <p class="details">www.tarikhosseny.com</p>
  </section>

  <section class="card card--front" aria-label="card front">
    <div class="panel">
      <h1 class="name">tarik b. hosseny</h1>
    </div>
    <p class="details">
      writer | photographer<br>
      get@tarikhosseny.com
    </p>
  </section>

</main>
</body>
</html>
```